PI Planning App Background Image

We need a newss background design (current one attached) that is used for an App on a big Touchscreen, on iOS and Windows.

The App will replace work on big walls with Flipcharts and Sticky-Notes. See the attached "empty" file that shows 6 "flipcharts" 4 of them for Iterations (an area for different color sticky notes), 1 for Risks (an area to place red sticky notes), 1 for Objectives (an area where text is added on the left area and a number (BV) on the right area.

You can see an example of "in use" attached.

We are looking for a background design. Nice and clear and as close to the real "wall, flipchart, sticky-notes" as possible.

Target Market(s)

Enterprises that do distributed TEMo PI Planning (also called Big Room Planning)

Requirements
Must have
• see above
Nice to have
• see above
Should not have
• see above

```html
<!DOCTYPE html>
<html lang="en">
<head>
<meta charset="utf-8">
<title>Planning Wall Background</title>
<style>
:root{
  --page:#ffffff;
  --header:#e9e9e9;
  --rule:#6d6d6d;
  --footer:#8a8a8a;
  --sheet:#f6f6f6;
  --shadow:rgba(0,0,0,.7);
  --c1:#5d4518; --n1:#a0926a;
  --c2:#8a8a48; --n2:#c4b887;
  --c3:#6a4380; --n3:#c69cc0;
  --c4:#4e7a93; --n4:#a2b8c4;
  --c5:#3f5a38;
  --c6:#6a6338;
  --c7:#17506c;
  --c8:#a65e55;
}
html,body{margin:0;width:1200px;height:960px;overflow:hidden;background:var(--page);}
.wall{position:absolute;left:44px;top:108px;width:1112px;height:714px;box-shadow:6px 6px 4px var(--shadow);background:var(--page);}
.wall-header{position:absolute;left:0;top:0;width:100%;height:46px;background:var(--header);border-top:2px solid var(--rule);border-bottom:2px solid var(--rule);box-sizing:border-box;}
.wall-footer{position:absolute;left:0;bottom:0;width:100%;height:27px;background:var(--footer);}
.flipchart{position:absolute;width:272px;height:304px;background:linear-gradient(90deg,#f3f3f3,#fafafa 40%,#f5f5f5);}
.corner{position:absolute;width:100%;height:100%;left:0;top:0;}
.note{position:absolute;width:113px;height:113px;border-radius:22px;box-shadow:3px 3px 3px var(--shadow);}
</style>
</head>
<body>
<main class="wall">
  <div class="wall-header"></div>

  <section class="flipchart" style="left:0;top:58px;--c:var(--c1)">
    <svg class="corner" viewBox="0 0 272 304"><g fill="var(--c1)"><polygon points="0,0 99,0 86,13 13,13 13,86 0,99"/><polygon points="272,304 173,304 186,291 259,291 259,218 272,205"/></g></svg>
    <div class="note" style="left:30px;top:34px;background:var(--n1)"></div>
    <div class="note" style="left:136px;top:165px;background:var(--n1)"></div>
  </section>
  <section class="flipchart" style="left:280px;top:58px">
    <svg class="corner" viewBox="0 0 272 304"><g fill="var(--c2)"><polygon points="0,0 99,0 86,13 13,13 13,86 0,99"/><polygon points="272,304 173,304 186,291 259,291 259,218 272,205"/></g></svg>
    <div class="note" style="left:27px;top:25px;background:var(--n2)"></div>
    <div class="note" style="left:132px;top:156px;background:var(--n2)"></div>
  </section>
  <section class="flipchart" style="left:560px;top:58px">
    <svg class="corner" viewBox="0 0 272 304"><g fill="var(--c3)"><polygon points="0,0 99,0 86,13 13,13 13,86 0,99"/><polygon points="272,304 173,304 186,291 259,291 259,218 272,205"/></g></svg>
    <div class="note" style="left:27px;top:31px;background:var(--n3)"></div>
    <div class="note" style="left:132px;top:161px;background:var(--n3)"></div>
  </section>
  <section class="flipchart" style="left:840px;top:58px">
    <svg class="corner" viewBox="0 0 272 304"><g fill="var(--c4)"><polygon points="0,0 99,0 86,13 13,13 13,86 0,99"/><polygon points="272,304 173,304 186,291 259,291 259,218 272,205"/></g></svg>
    <div class="note" style="left:27px;top:31px;background:var(--n4)"></div>
    <div class="note" style="left:132px;top:161px;background:var(--n4)"></div>
  </section>

  <section class="flipchart" style="left:0;top:375px">
    <svg class="corner" viewBox="0 0 272 304"><g fill="var(--c5)"><polygon points="0,0 99,0 86,13 13,13 13,86 0,99"/><polygon points="272,304 173,304 186,291 259,291 259,218 272,205"/></g></svg>
  </section>
  <section class="flipchart" style="left:280px;top:375px">
    <svg class="corner" viewBox="0 0 272 304"><g fill="var(--c6)"><polygon points="0,0 99,0 86,13 13,13 13,86 0,99"/><polygon points="272,304 173,304 186,291 259,291 259,218 272,205"/></g></svg>
  </section>
  <section class="flipchart" style="left:560px;top:375px">
    <svg class="corner" viewBox="0 0 272 304"><g fill="var(--c7)"><polygon points="0,0 99,0 86,13 13,13 13,86 0,99"/><polygon points="272,304 173,304 186,291 259,291 259,218 272,205"/></g></svg>
  </section>
  <section class="flipchart" style="left:840px;top:375px">
    <svg class="corner" viewBox="0 0 272 304"><g fill="var(--c8)"><polygon points="0,0 99,0 86,13 13,13 13,86 0,99"/><polygon points="272,304 173,304 186,291 259,291 259,218 272,205"/></g></svg>
  </section>

  <div class="wall-footer"></div>
</main>
</body>
</html>
```